Ridgewell Hauling Business Cards & Stantionery
Dump Truck Services
Ridgewell Hauling Business Cards & Stantionery -
Creative Brief
Professional
Osvaldo Mireles, Jr.
Owner
4158 Fenwick Rd. Pearland, TX 77590
osvaldo@ridgewellhauling-demo.com
www.ridgewellhauling-demo.com

```html
<!DOCTYPE html>
<html lang="en">
<head>
<meta charset="utf-8">
<title>Ridgewell Hauling Stationery</title>
<link href="https://fonts.googleapis.com/css2?family=Roboto+Condensed:wght@400;700&display=swap" rel="stylesheet">
<style>
  :root {
    --board: #2a2b2d;
    --board-dark: #1c1d1f;
    --paper: #ffffff;
    --red: #d7141d;
    --red-dark: #a50d14;
    --blue: #1f4fa3;
    --ink: #2b2b2b;
    --muted: #8a8a8a;
    --faint: rgba(215, 20, 29, 0.08);
  }
  * { box-sizing: border-box; margin: 0; padding: 0; }
  html, body { width: 1200px; height: 310px; overflow: hidden; }
  body {
    background: radial-gradient(ellipse at center, var(--board) 0%, var(--board-dark) 100%);
    font-family: "Roboto Condensed", Arial, sans-serif;
    color: var(--ink);
    position: relative;
  }
  .piece { position: absolute; background: var(--paper); overflow: hidden; box-shadow: 0 2px 6px rgba(0,0,0,.5); }
  .swoosh { position: absolute; left: 0; bottom: 0; width: 100%; }
  .brand { display: flex; align-items: center; gap: 3px; font-weight: 700; color: var(--red); text-transform: uppercase; white-space: nowrap; line-height: 1; }
  .brand .dot { border-radius: 50%; background: var(--red); flex: none; }

  .board-logo { position: absolute; left: 22px; top: 42px; }
  .board-logo .brand { font-size: 15px; }
  .board-logo .dot { width: 14px; height: 14px; }
  .board-logo .tagline { color: #bbb; font-size: 7px; margin: 3px 0 0 17px; }

  .card { width: 101px; height: 60px; }
  .card-front { left: 19px; top: 113px; }
  .card-back { left: 132px; top: 113px; }
  .card-plain { left: 19px; top: 209px; }
  .card-red { left: 132px; top: 209px; background: var(--red); display: flex; align-items: center; justify-content: center; }
  .card .brand { font-size: 7px; }
  .card .dot { width: 7px; height: 7px; }
  .card-front .brand { position: absolute; left: 6px; top: 8px; }
  .card-front .contact { position: absolute; right: 6px; top: 26px; font-size: 3.6px; text-align: right; color: var(--muted); line-height: 1.4; }
  .card-back .person { position: absolute; left: 6px; top: 8px; font-size: 5px; font-weight: 700; }
  .card-back .role { font-weight: 400; color: var(--muted); font-size: 4px; }
  .card-back .contact { position: absolute; left: 6px; top: 24px; font-size: 3.6px; color: var(--muted); line-height: 1.4; }
  .card-back .brand { position: absolute; right: 6px; top: 8px; font-size: 5px; }
  .card-back .dot { width: 5px; height: 5px; }
  .card-plain { display: flex; align-items: center; justify-content: flex-start; padding-left: 8px; }
  .card-red .brand { color: var(--paper); font-size: 8px; }
  .card-red .dot { background: var(--paper); width: 8px; height: 8px; }

  .letterhead { width: 120px; height: 158px; top: 19px; }
  .letterhead-one { left: 355px; }
  .letterhead-two { left: 492px; }
  .letterhead .brand { position: absolute; left: 10px; top: 9px; font-size: 7px; }
  .letterhead .dot { width: 7px; height: 7px; }
  .letterhead .contact { position: absolute; right: 9px; top: 8px; font-size: 3.4px; color: var(--muted); text-align: right; line-height: 1.4; }
  .letterhead .mark { position: absolute; left: 30px; top: 50px; width: 60px; height: 60px; border-radius: 50%; background: var(--faint); }

  .compliment { left: 643px; width: 150px; }
  .compliment-one { top: 55px; height: 94px; }
  .compliment-two { top: 168px; height: 100px; }
  .compliment .brand { position: absolute; left: 10px; top: 10px; font-size: 7px; }
  .compliment .dot { width: 7px; height: 7px; }
  .compliment .contact { position: absolute; right: 10px; top: 9px; font-size: 3.4px; color: var(--muted); text-align: right; line-height: 1.4; }

  .envelope { left: 816px; width: 172px; }
  .envelope-blue { top: 52px; height: 86px; background: var(--blue); }
  .envelope-flap { top: 122px; height: 90px; }
  .envelope-back { top: 206px; height: 74px; }
  .envelope-blue .brand { position: absolute; left: 50%; top: 24px; transform: translateX(-50%); color: var(--paper); font-size: 8px; }
  .envelope-blue .dot { background: var(--paper); width: 8px; height: 8px; }
  .envelope-flap svg.flap, .envelope-back svg.flap { position: absolute; left: 0; top: 0; width: 100%; height: 100%; }
  .envelope-flap .brand { position: absolute; left: 50%; top: 36px; transform: translateX(-50%); font-size: 7px; }
  .envelope-flap .dot { width: 7px; height: 7px; }
</style>
</head>
<body>

<svg width="0" height="0" style="position:absolute">
  <defs>
    <symbol id="wave" viewBox="0 0 100 20" preserveAspectRatio="none">
      <path d="M0 12 C30 2 60 22 100 6 L100 20 L0 20 Z" fill="#1f4fa3"/>
      <path d="M0 15 C30 6 60 24 100 10 L100 20 L0 20 Z" fill="#d7141d"/>
    </symbol>
  </defs>
</svg>

<div class="board-logo">
  <div class="brand"><span class="dot"></span>Ridgewell Hauling</div>
  <div class="tagline">Dump Truck Services</div>
</div>

<div class="piece card card-front">
  <div class="brand"><span class="dot"></span>Ridgewell Hauling</div>
  <div class="contact">4158 Fenwick Rd. Pearland, TX 77590<br>osvaldo@ridgewellhauling-demo.com<br>www.ridgewellhauling-demo.com</div>
  <svg class="swoosh" height="12"><use href="#wave"/></svg>
</div>

<div class="piece card card-back">
  <div class="person">Osvaldo Mireles, Jr.<br><span class="role">Owner</span></div>
  <div class="contact">4158 Fenwick Rd. Pearland, TX 77590<br>osvaldo@ridgewellhauling-demo.com<br>www.ridgewellhauling-demo.com</div>
  <div class="brand"><span class="dot"></span>Ridgewell</div>
  <svg class="swoosh" height="12"><use href="#wave"/></svg>
</div>

<div class="piece card card-plain">
  <div class="brand"><span class="dot"></span>Ridgewell Hauling</div>
</div>

<div class="piece card card-red">
  <div class="brand"><span class="dot"></span>Ridgewell Hauling</div>
</div>

<div class="piece letterhead letterhead-one">
  <div class="brand"><span class="dot"></span>Ridgewell Hauling</div>
  <div class="contact">4158 Fenwick Rd.<br>Pearland, TX 77590<br>www.ridgewellhauling-demo.com</div>
  <div class="mark"></div>
  <svg class="swoosh" height="16"><use href="#wave"/></svg>
</div>

<div class="piece letterhead letterhead-two">
  <div class="brand"><span class="dot"></span>Ridgewell Hauling</div>
  <div class="contact">4158 Fenwick Rd.<br>Pearland, TX 77590<br>www.ridgewellhauling-demo.com</div>
  <div class="mark"></div>
  <svg class="swoosh" height="16"><use href="#wave"/></svg>
</div>

<div class="piece compliment compliment-one">
  <div class="brand"><span class="dot"></span>Ridgewell Hauling</div>
  <div class="contact">4158 Fenwick Rd.<br>Pearland, TX 77590</div>
</div>

<div class="piece compliment compliment-two">
  <div class="brand"><span class="dot"></span>Ridgewell Hauling</div>
  <div class="contact">4158 Fenwick Rd.<br>Pearland, TX 77590</div>
  <svg class="swoosh" height="18"><use href="#wave"/></svg>
</div>

<div class="piece envelope envelope-blue">
  <div class="brand"><span class="dot"></span>Ridgewell Hauling</div>
  <svg class="swoosh" height="14" viewBox="0 0 100 20" preserveAspectRatio="none"><path d="M0 14 C30 4 60 24 100 8 L100 20 L0 20 Z" fill="#d7141d"/></svg>
</div>

<div class="piece envelope envelope-flap">
  <svg class="flap" viewBox="0 0 172 90" preserveAspectRatio="none"><path d="M0 0 L86 34 L172 0" fill="none" stroke="#d9d9d9" stroke-width="1"/></svg>
  <div class="brand"><span class="dot"></span>Ridgewell</div>
</div>

<div class="piece envelope envelope-back">
  <svg class="flap" viewBox="0 0 172 74" preserveAspectRatio="none"><path d="M0 0 L86 30 L172 0 M0 74 L70 40 M172 74 L102 40" fill="none" stroke="#d9d9d9" stroke-width="1"/></svg>
</div>

</body>
</html>
```